Trade Show Package: Logo, B. Card, Brochure, T Shirt & Signs

We have a trade show coming up and will need the following designed: tri-fold, logo cleanup, business cards, t-shirt text and 6 poster signs.

We want all our materials to be consistent, modern (san serif fonts) contemporary and clean. You can take a look at our website, www.bright-lane-webworks.com to see the color scheme we are using and overall look (we use dark red, grey, black, charcoal grey).

1- Logo Cleanup
Our logo is attached. It needs to be cleaned up and sharp so that it looks really good on all of our materials.
We need a thin red line added to the bottom of the logo. See the logo on the tri-fold on the bottom right.
Perhaps the tagline, business on skyforge88 should be a lighter charcoal grey.

If you have any ideas that you think would make it better, of course we welcome that.

We need the logo cleaned up first as the logo is needed for the business cards, tri-fold, t-shirts and signs.

2- Business Cards
Our business cards will be printed on white paper.
Top has a dark red border, followed by our logo (with thin red line underneath) followed by text.

Here is a screencast of what we are going for: http://clipvault-demo.net/t/QxR7p2kWdnLa
We'll need the two separate cards shown in the screencast.

BASIC STYLE: clean, modern design

FONT: modern, easy to read

COLORS: dark red for the bar at the top (full bleed) and Marcus's name & possibly charcoal grey for the rest of the text

3- Tri-fold
3 (5x7 panels) brochure

This brochure is all about cloud computing. I have attached a plain pdf that I put together just to show the order of the tri-fold; this is not the design we
want, we want a modern design, clean, consistent colors and look.

We have 2 pictures we found but if you think another picture would work better for the design, please
show us your ideas.

Here is what we are looking for:

COLOR: will be printed on white paper, except one page will be black (testimonials page, full bleed);
also we need to have a spot uv on the front and back covers and we want a font that does well with that. The video with the black brochure will show the spot uv we are looking for.

BASIC STYLE: clean, modern and innovative

FONT: modern, easy to read and shows up well on paper (san serif fonts)

Left inside trifold: man in a brown box working - see link I provided at the bottom of that page; let me know the size you require and I'll purchase it and email it to you. We want this page to match or complement the coloring of the rest of our brochure, maybe something like this (reddish overtones? instead of the brown which doesn't go). Picture full bleed.

Middle inside: man lying on grass, dreaming of bubble - see link I provided at the bottom of that page; let me know the size you require and I'll purchase it and email it to you. Picture full bleed.

Right inside: text (boost business with cloud computing) with our logo on the bottom right (the word "might" needs to be in italics)

Outside left: the testimonials goes here, make background black (this page only) with white or other light text, full black bleed

Outside middle: BACK COVER - our logo and address

Outside right: FRONT COVER - text (get your cloud on) and our logo on bottom right (with the thin red line underneath)

4- Shirts
T-SHIRT FRONT: our logo on left side

T-SHIRT BACK:
Ask Me (should be biggest font size and in red)
about (should be on second line and smaller in black)
Cloud Computing (should be on the third line, black text and smaller than ask me but big)

- find a graphical element from our logo and use it here, for example the red line, to make it easier to read and make it interesting
- should be modern (consistent with the rest of our materials, i.e. brochure ...)
- attached a sample look we put together but we need a designed modern look

5- Signs
Here is a preliminary look at our signs (pdf attached), last 2 slides will be updated slightly and sent back to you with dimensions for all the signs.

Text should be 1 1/2 inches from the frames border. Will be printed on a white background.

BASIC STYLE: clean, modern design (something that will draw people to look at the sign)
the thick red rectangle on the bottom with the logo on the right should be more interesting, maybe add gradient, texture, etc.

FONT: modern, easy to read (san serif fonts) first 4 posters should be the same exact font and size.

COLORS: dark red, black, greys, charcoal grey

NOTE: We will only guarantee payment once we see designs that match our criteria. We cannot guarantee until we have SEEN your work.

```html
<!DOCTYPE html>
<html lang="en">
<head>
<meta charset="utf-8">
<title>Bright Lane Webworks – Logo and Business Cards</title>
<link rel="stylesheet" href="https://fonts.googleapis.com/css2?family=Source+Sans+3:ital,wght@0,300;0,400;0,600;0,700;1,300&display=swap">
<style>
  :root {
    --brand-red: #c8000a;
    --ink: #111111;
    --charcoal: #6b6b6b;
    --text-grey: #707070;
    --card-edge: #bdbdbd;
    --paper: #ffffff;
  }
  * { box-sizing: border-box; margin: 0; padding: 0; }
  html, body {
    width: 1200px; height: 900px; overflow: hidden;
    background: var(--paper);
    font-family: "Source Sans 3", "Myriad Pro", Arial, sans-serif;
  }
  .sheet { position: relative; width: 1200px; height: 900px; }

  /* Wordmark */
  .wordmark { position: absolute; }
  .wordmark__name {
    color: var(--ink); font-weight: 700; letter-spacing: -0.02em; line-height: 0.92;
  }
  .wordmark__tagline {
    color: var(--charcoal); font-weight: 600; text-align: right;
  }
  .wordmark--large { left: 118px; top: 150px; width: 375px; }
  .wordmark--large .wordmark__name { font-size: 66px; }
  .wordmark--large .wordmark__tagline { font-size: 19px; margin-top: 10px; }

  .wordmark--card { left: 22px; top: 30px; width: 186px; }
  .wordmark--card .wordmark__name { font-size: 32px; }
  .wordmark--card .wordmark__tagline { font-size: 10px; margin-top: 5px; }

  /* Business cards */
  .card {
    position: absolute; width: 226px; height: 401px;
    border: 1px solid var(--card-edge); background: var(--paper);
  }
  .card__bar {
    position: absolute; left: -1px; right: -1px; top: -1px; height: 8px;
    background: var(--brand-red);
  }
  .card__rule {
    position: absolute; left: 29px; top: 135px; width: 60px; height: 2px;
    background: var(--brand-red);
  }
  .card__info {
    position: absolute; left: 23px; right: 8px;
    font-size: 14.5px; font-weight: 300; line-height: 19.5px; color: var(--text-grey);
  }
  .card__info p + p { margin-top: 19.5px; }
  .card__name { color: var(--brand-red); font-weight: 400; }
  .card__role { font-style: italic; }

  .card--personal .card__info { top: 186px; }
  .card--general .card__info { top: 226px; }

  .card--a { left: 649px; top: 32px; }
  .card--b { left: 907px; top: 32px; }
  .card--c { left: 649px; top: 466px; }
  .card--d { left: 907px; top: 466px; }
</style>
</head>
<body>
<main class="sheet">

  <div class="wordmark wordmark--large">
    <div class="wordmark__name">bright-lane-<br>webworks</div>
    <div class="wordmark__tagline">business on skyforge88</div>
  </div>

  <article class="card card--personal card--a">
    <div class="card__bar"></div>
    <div class="wordmark wordmark--card">
      <div class="wordmark__name">bright-lane-<br>webworks</div>
      <div class="wordmark__tagline">business on skyforge88</div>
    </div>
    <div class="card__rule"></div>
    <div class="card__info">
      <p><span class="card__name">Marcus Delaney</span><br><span class="card__role">Founding Owner</span><br>mdelaney@bright-lane-webworks.com</p>
      <p>www.bright-lane-webworks.com<br>4120 Harbor Ave., Suite 210 UL<br>Maple Ridge, NY 11492<br>555-014-2297</p>
    </div>
  </article>

  <article class="card card--personal card--b">
    <div class="card__bar"></div>
    <div class="wordmark wordmark--card">
      <div class="wordmark__name">bright-lane-<br>webworks</div>
      <div class="wordmark__tagline">business on skyforge88</div>
    </div>
    <div class="card__rule"></div>
    <div class="card__info">
      <p><span class="card__name">Marcus Delaney</span><br><span class="card__role">Founding Owner</span><br>mdelaney@bright-lane-webworks.com</p>
      <p>www.bright-lane-webworks.com<br>4120 Harbor Ave., Suite 210 UL<br>Maple Ridge, NY 11492<br>555-014-2297</p>
    </div>
  </article>

  <article class="card card--general card--c">
    <div class="card__bar"></div>
    <div class="wordmark wordmark--card">
      <div class="wordmark__name">bright-lane-<br>webworks</div>
      <div class="wordmark__tagline">business on skyforge88</div>
    </div>
    <div class="card__rule"></div>
    <div class="card__info">
      <p>www.bright-lane-webworks.com<br>4120 Harbor Ave., Suite 210 UL<br>Maple Ridge, NY 11492</p>
      <p>555-014-2297</p>
      <p>info@bright-lane-webworks.com</p>
    </div>
  </article>

  <article class="card card--general card--d">
    <div class="card__bar"></div>
    <div class="wordmark wordmark--card">
      <div class="wordmark__name">bright-lane-<br>webworks</div>
      <div class="wordmark__tagline">business on skyforge88</div>
    </div>
    <div class="card__rule"></div>
    <div class="card__info">
      <p>www.bright-lane-webworks.com<br>4120 Harbor Ave., Suite 210 UL<br>Maple Ridge, NY 11492</p>
      <p>555-014-2297</p>
      <p>info@bright-lane-webworks.com</p>
    </div>
  </article>

</main>
</body>
</html>
```